Business Card for Pottery and Jewellery Designer

A new business card design is needed to accompany a newly launching pottery and jewellery website. The company logo has been attached for use. The company is called Kilnwick Lane. For a sense of the vibe please see the website (it is currently under construction but this way you'll get a feel for the style) www.KilnwickLane.com

The website font is Pontano Sans for the body of the text with Overlock for headers.

The overall look should be clean and elegant. The back side can have just the logo. The front side should have a smaller logo and the following details displayed:

Kilnwick Lane
Designer: Marisol Bexley
Phone: xxx.xxx.xxxx
Email: Designer@KilnwickLane.com

The structure of displaying this is completely up to you. Different layouts and creative methods of displaying contact info are welcome as long as it stays clean/uncluttered.

No product photographs are to be included in the design as the catalogue changes quickly.

Colour preferences lean towards elegant and understated (charcoal grey, dark navy blue etc.)

Please let me know if you have any further questions or further details required.

Target Market(s)

Target market is 30+ year old women

Industry/Entity Type

Construction

Colors
ffffff
1b1b1b
474747
d9d9d9
fafafa
0355a3

Requirements
Must have
• The submissions so far have looked very typical and don't stand out right now. They're also all in navy with very little variation. I'm looking for something that stands out a it more while still being clean-looking.
Nice to have
• I've attached a few design samples and an idea for a backdrop. It would be great to see some designs in black, white, and grey with only a hint of color.
Should not have
• Product Images

```html
<!DOCTYPE html>
<html lang="en">
<head>
<meta charset="utf-8">
<title>Kilnwick Lane – Business Card</title>
<link rel="stylesheet" href="https://fonts.googleapis.com/css2?family=Cinzel:wght@400;500&family=Cormorant+Garamond:ital,wght@0,500;1,400&display=swap">
<style>
  :root {
    --backdrop: #d9d9d9;
    --card: #fafafa;
    --card-edge: #efefef;
    --ink: #1b1b1b;
    --charcoal: #474747;
    --grey: #8a8a8a;
    --rule: #d9d9d9;
    --accent: #0355a3;
    --shadow: rgba(27, 27, 27, 0.2);
  }
  * { box-sizing: border-box; margin: 0; padding: 0; }
  html, body {
    width: 1200px; height: 900px; overflow: hidden;
    background: var(--backdrop);
    font-family: "Cinzel", "Times New Roman", serif;
    color: var(--ink);
  }
  .canvas { position: relative; width: 1200px; height: 900px; }

  .card {
    position: absolute;
    width: 600px; height: 345px;
    border-radius: 16px;
    background: linear-gradient(160deg, #ffffff 0%, var(--card) 55%, var(--card-edge) 100%);
    box-shadow: 0 10px 30px var(--shadow);
    overflow: hidden;
  }
  .card--back { left: 70px; top: 70px; }
  .card--front { left: 530px; top: 480px; }

  /* Wordmark */
  .wordmark {
    position: absolute; inset: 0;
    display: flex; align-items: center; justify-content: center; gap: 22px;
  }
  .wordmark__dot {
    flex: none;
    width: 40px; height: 40px; border-radius: 50%;
    background: var(--accent);
  }
  .wordmark__name {
    color: var(--ink);
    font-weight: 400;
    font-size: 46px;
    line-height: 1.05;
    letter-spacing: 6px;
    text-transform: uppercase;
    text-align: center;
  }

  /* Front */
  .front__brand {
    position: absolute; left: 34px; top: 40px;
    display: flex; align-items: center; gap: 12px;
  }
  .front__brand .wordmark__dot { width: 22px; height: 22px; }
  .front__brand .wordmark__name { font-size: 22px; letter-spacing: 3px; text-align: left; }

  .person {
    position: absolute; right: 36px; top: 30px; text-align: right;
  }
  .person__name {
    font-size: 17px; letter-spacing: 1px; color: var(--ink);
    text-transform: uppercase;
  }
  .person__role {
    font-family: "Cormorant Garamond", "Times New Roman", serif;
    font-style: italic; font-size: 30px; color: var(--grey);
    margin-top: -2px; margin-right: 6px;
  }

  .contact {
    position: absolute; left: 200px; top: 150px;
    list-style: none;
    font-family: "Cormorant Garamond", "Times New Roman", serif;
    font-weight: 500; font-size: 17px; color: var(--ink);
  }
  .contact li { display: flex; align-items: center; gap: 10px; height: 26px; }
  .contact svg { width: 16px; height: 14px; fill: var(--charcoal); }
  .contact__web { color: var(--grey); padding-left: 2px; }

  .accent-rule {
    position: absolute; left: 190px; top: 232px; width: 380px; height: 3px;
    background: linear-gradient(90deg, transparent 0%, var(--accent) 45%, var(--rule) 80%, transparent 100%);
  }
  .fine-rule {
    position: absolute; left: 40px; right: 40px; top: 264px; height: 1px;
    background: linear-gradient(90deg, transparent, var(--rule) 20%, var(--rule) 80%, transparent);
  }
  .tagline {
    position: absolute; left: 0; right: 0; top: 276px;
    text-align: center; font-size: 12.5px; line-height: 1.7;
    letter-spacing: 0.6px; text-transform: uppercase; color: var(--charcoal);
  }
</style>
</head>
<body>
<main class="canvas">
  <section class="card card--back" aria-label="Card back">
    <div class="wordmark">
      <span class="wordmark__dot"></span>
      <span class="wordmark__name">Kilnwick<br>Lane</span>
    </div>
  </section>

  <section class="card card--front" aria-label="Card front">
    <div class="front__brand">
      <span class="wordmark__dot"></span>
      <span class="wordmark__name">Kilnwick<br>Lane</span>
    </div>

    <div class="person">
      <p class="person__name">Marisol Bexley</p>
      <p class="person__role">Designer</p>
    </div>

    <ul class="contact">
      <li>
        <svg viewBox="0 0 16 14" aria-hidden="true"><path d="M1 4c0-2 3-3 7-3s7 1 7 3v1h-4V3.5H5V5H1z"/><rect x="2.5" y="6" width="11" height="7" rx="1.5"/></svg>
        <span>1300 555 014</span>
      </li>
      <li>
        <svg viewBox="0 0 16 14" aria-hidden="true"><path d="M0 2h16v10H0z M1.5 3.3 8 8.3l6.5-5z" fill-rule="evenodd"/></svg>
        <span>Designer@KilnwickLane.com</span>
      </li>
      <li class="contact__web">www.KilnwickLane.com</li>
    </ul>

    <div class="accent-rule"></div>
    <div class="fine-rule"></div>

    <p class="tagline">Kilnwick Lane offers hand<br>crafted designer jewellery, pottery and artwork.</p>
  </section>
</main>
</body>
</html>
```